Property Finance Company - Orin Ventures Limited

Background: Orin Ventures Group Limited is a private property finance company. Orin Ventures Group has capital to directly fund first mortgage, mezzanine and preferred equity financing. We also acquire performing, sub-performing and distressed debt.

Orin Ventures' management philosophy emphasises expertise, innovation, wisdom, honesty and competitiveness. Orin Ventures are not finance brokers - we provide debt funding to the commercial property and residential development sectors. Our process is built from experience and cumutavely Orin Ventures' Directors have in excess of 60 years wisdom.

The aim of the website will be to increase brand awareness, provide clients with comfort around our level of skill and background on who we are, generate more sales, and provide examples of projects that we have funded.

The website is a new product launch, and we need to use our Orin Ventures logo that has just been designed. We like a dark background, and either black/silver/grey/ jade green, or black/gold/jade green colours.

Our unique advantages are that we have fast turnaround times, we can solve clients funding problems and we know what we are doing. Our target audience will be viewing the website on both desktop and mobile devices.

We would like to have the following pages:

Home
About
Team
Services
Project Experience
Contact

Competitors Website: http://www.tarvelo.com/

We would also like to have the option of video footage in our website, as you can see in our competitors website.

Overall we want a really slick, elegant but modern website that is better than www.tarvelo.com

Target Market(s)

Finance borrowers, property developers, accountants, lawyers, businesspeople, high net worth people

Industry/Entity Type

Finance

Requirements
Must have
• Please see project description
Nice to have
Should not have

```html
<!DOCTYPE html>
<html lang="en">
<head>
<meta charset="utf-8">
<title>Orin Ventures Group</title>
<link href="https://fonts.googleapis.com/css2?family=Lato:wght@300;400;700&family=Open+Sans:wght@400;600&display=swap" rel="stylesheet">
<style>
:root{
  --teal:#3aa99b;
  --teal-dark:#2f8f83;
  --teal-light:#5cc0b3;
  --ink:#3b3b3b;
  --muted:#6b6b6b;
  --rule:#dcdcdc;
  --dark:#2f2f2f;
  --darker:#262626;
  --darkest:#1f1f1f;
  --white:#ffffff;
  --soft:#cfcfcf;
}
*{box-sizing:border-box;margin:0;padding:0}
html,body{width:1200px;height:3930px;overflow:hidden}
body{font-family:'Open Sans',sans-serif;color:var(--ink);background:var(--white);position:relative}
.abs{position:absolute}
section,header,nav,footer{position:absolute;left:0;width:1200px}
.heading{font-family:'Lato',sans-serif;font-weight:400;font-size:32px;text-transform:uppercase;text-align:center;position:absolute;left:0;width:1200px}
.heading-rule{position:absolute;left:79px;width:1042px;height:1px;background:var(--rule)}
.heading-rule::after{content:"";position:absolute;left:471px;top:-1px;width:100px;height:3px;background:var(--teal)}

/* hero */
.hero{top:0;height:686px;background:linear-gradient(120deg,#4d5358 0%,#6b7074 40%,#7d7f80 60%,#55595c 100%)}
.hero-shade{position:absolute;inset:0;background:rgba(30,32,34,.45)}
.brand{position:absolute;top:448px;left:0;width:1200px;text-align:center;font-family:'Lato',sans-serif;font-weight:400;font-size:66px;letter-spacing:4px;color:var(--white)}

/* nav */
.main-nav{top:686px;height:66px;background:var(--teal)}
.main-nav a{position:absolute;top:20px;font-family:'Lato',sans-serif;font-size:18px;color:var(--white);text-decoration:none}
.main-nav a.active::after{content:"";position:absolute;left:0;right:0;bottom:-21px;height:3px;background:var(--white)}
.contact-btn{position:absolute;left:956px;top:11px;width:165px;height:44px;border:2px solid var(--white);border-radius:22px;color:var(--white);font-family:'Lato',sans-serif;font-size:18px;text-align:center;line-height:40px}

/* welcome */
.welcome{top:752px;height:519px}
.intro{position:absolute;top:132px;left:130px;width:940px;text-align:center;font-size:14px;line-height:26px;color:var(--muted)}
.value{position:absolute;top:250px;width:250px}
.value-num{font-family:'Lato',sans-serif;font-weight:300;font-size:42px;color:var(--teal);line-height:50px}
.value-title{display:flex;align-items:center;gap:12px;font-family:'Lato',sans-serif;font-size:20px;color:var(--ink);margin-top:4px}
.value-title::after{content:"";flex:1;height:2px;background:var(--teal)}
.value p{font-size:14px;line-height:24px;color:var(--muted);margin-top:6px}
.value-foot{margin-top:22px;border-top:1px solid var(--rule);border-bottom:1px solid var(--rule);height:5px}

/* services */
.services{top:1271px;height:521px;background:var(--dark);color:var(--white)}
.services .heading{color:var(--white);font-weight:700;font-size:30px}
.services .heading-rule{background:#505050}
.service{position:absolute;width:330px}
.service h3{font-family:'Lato',sans-serif;font-weight:700;font-size:22px;margin-bottom:10px}
.service p{font-size:14px;line-height:26px;color:var(--soft)}
.service.left{text-align:right}
.svc-icon{position:absolute;width:112px;height:112px}
.cross-v{position:absolute;left:599px;top:253px;width:1px;height:150px;background:#4a4a4a}
.cross-h{position:absolute;left:524px;top:328px;width:150px;height:1px;background:#4a4a4a}

/* team */
.team{top:1792px;height:540px}
.member{position:absolute;top:144px;width:240px;height:320px;border:2px solid #e2e2e2;text-align:center}
.member.featured{border-color:var(--teal)}
.portrait{position:absolute;left:14px;top:14px;width:208px;height:204px;background:linear-gradient(160deg,#b9c0c6,#5d6670 70%,#3a3f45)}
.member h4{position:absolute;top:232px;left:0;width:100%;font-family:'Lato',sans-serif;font-weight:400;font-size:20px;color:var(--ink)}
.member span{position:absolute;top:266px;left:0;width:100%;font-size:13px;color:var(--muted)}
.member i{position:absolute;top:294px;left:100px;width:36px;height:5px;border-top:1px solid #999;border-bottom:1px solid #999}

/* testimonials */
.clients{top:2332px;height:440px;background:var(--dark)}
.clients .heading{color:var(--white);font-weight:700;font-size:30px}
.clients .heading-rule{background:#505050}
.quote-card{position:absolute;top:178px;width:322px;height:183px;background:var(--darker);text-align:center;padding:50px 22px 0}
.quote-card p{font-size:14px;line-height:24px;color:var(--white)}
.quote-card em{display:block;font-style:normal;color:var(--teal);font-size:16px;margin-top:14px}
.quote-mark{position:absolute;top:-34px;left:127px;width:68px;height:68px}

/* news */
.news{top:2772px;height:521px}
.article{position:absolute;top:141px;width:322px}
.article-img{width:322px;height:200px;background:linear-gradient(135deg,#d7dde2,#7a8794 60%,#3e4750)}
.article-body{display:flex;gap:14px;margin-top:23px}
.date{flex:0 0 60px;height:80px;background:var(--teal);color:var(--white);text-align:center;font-family:'Lato',sans-serif}
.date b{display:block;font-size:28px;font-weight:400;line-height:48px}
.date small{font-size:14px;font-weight:700}
.article h5{font-family:'Lato',sans-serif;font-weight:700;font-size:15px;color:var(--ink);margin-bottom:6px}
.article p{font-size:13px;line-height:23px;color:var(--muted)}

/* signup */
.signup{top:3293px;height:105px;background:var(--teal)}
.signup h3{position:absolute;left:79px;top:36px;font-family:'Lato',sans-serif;font-weight:700;font-size:22px;color:var(--white)}
.signup .field{position:absolute;left:694px;top:30px;width:289px;height:44px;background:var(--teal-dark);color:#d8efec;font-size:14px;line-height:44px;padding-left:14px}
.signup .go{position:absolute;left:996px;top:30px;width:125px;height:44px;background:var(--teal-light);color:var(--white);font-family:'Lato',sans-serif;font-weight:700;font-size:16px;line-height:44px;text-align:center;text-transform:uppercase}

/* footer */
.site-footer{top:3398px;height:393px;background:var(--dark);color:var(--white)}
.contact-box{position:absolute;left:79px;top:63px;width:306px;height:265px;border:1px solid #5a5a5a;padding:30px 22px}
.contact-box h4{font-family:'Lato',sans-serif;font-weight:700;font-size:18px;text-transform:uppercase}
.contact-box h4::after{content:"";display:block;width:70px;height:2px;background:var(--teal);margin-top:14px}
.contact-line{display:flex;gap:14px;font-size:14px;line-height:24px;margin-top:18px}
.contact-line svg{flex:0 0 18px;margin-top:3px}
.quote-title{position:absolute;left:445px;top:62px;font-family:'Lato',sans-serif;font-weight:700;font-size:30px;text-transform:uppercase}
.quote-rule{position:absolute;left:445px;top:118px;width:676px;height:1px;background:#555}
.quote-rule::after{content:"";position:absolute;left:0;top:-1px;width:70px;height:3px;background:var(--teal)}
.input{position:absolute;background:var(--darker);color:#888;font-size:13px;padding:10px 14px}
.send{position:absolute;left:1058px;top:162px;width:63px;height:145px;background:var(--teal)}

/* bottom bar */
.bottom{top:3791px;height:139px;background:var(--darkest);text-align:center;color:var(--white)}
.bottom-links{margin-top:40px;display:flex;justify-content:center;gap:40px;font-size:14px}
.bottom p{margin-top:24px;font-size:13px;color:var(--soft)}
.bottom p b{color:var(--white)}
</style>
</head>
<body>

<header class="hero">
  <div class="abs" style="inset:0" role="img" aria-label="Photo of a businessman working at a laptop in a bright office"></div>
  <div class="hero-shade"></div>
  <div class="brand">ORIN VENTURES GROUP</div>
</header>

<nav class="main-nav">
  <a class="active" style="left:79px">Home</a>
  <a style="left:165px">About</a>
  <a style="left:257px">Team</a>
  <a style="left:343px">Services</a>
  <a style="left:448px">Project Experience</a>
  <a style="left:640px">Contact</a>
  <div class="contact-btn">CONTACT US</div>
</nav>

<section class="welcome">
  <h2 class="heading" style="top:46px">Welcome to Orin Ventures Group</h2>
  <div class="heading-rule" style="top:104px"></div>
  <p class="intro">Lorem ipsum dolor sit amet, consectetur adipiscing elit. Nam tempor faucibus ante, eget vulputate libero pharetra eu. Nulla at felis eros. Sed ut metus justo. Suspendisse vestibulum dui at magna rutrum vestibulum. Vestibulum ante ipsum primis in faucibus orci luctus et ultrices posuere cubilia Curae; Nullam eget blandit augue. Sed tempus sapien purus, ac sollicitudin sem porttitor a.</p>
  <div class="value" style="left:79px"><div class="value-num">01</div><div class="value-title">Innovation</div><p>Lorem ipsum dolor sit amet, conse adipiscing elit. Nam tempor faucib ante, eget vulputate libero.</p><div class="value-foot"></div></div>
  <div class="value" style="left:347px"><div class="value-num">02</div><div class="value-title">Wisdom</div><p>Lorem ipsum dolor sit amet, conse adipiscing elit. Nam tempor faucib ante, eget vulputate libero.</p><div class="value-foot"></div></div>
  <div class="value" style="left:615px"><div class="value-num">03</div><div class="value-title">Honesty</div><p>Lorem ipsum dolor sit amet, conse adipiscing elit. Nam tempor faucib ante, eget vulputate libero.</p><div class="value-foot"></div></div>
  <div class="value" style="left:883px"><div class="value-num">04</div><div class="value-title">Competitivenes</div><p>Lorem ipsum dolor sit amet, conse adipiscing elit. Nam tempor faucib ante, eget vulputate libero.</p><div class="value-foot"></div></div>
</section>

<section class="services">
  <h2 class="heading" style="top:38px">Our Best Services</h2>
  <div class="heading-rule" style="top:96px"></div>
  <div class="cross-v"></div><div class="cross-h"></div>

  <div class="service left" style="left:84px;top:162px"><h3>Debt funding</h3><p>Lorem ipsum dolor sit amet, consectetur adipiscing elit. Nam tempor faucibus ante, eget vulputate libero pharetra eu. Nulla at felis eros.</p></div>
  <div class="service" style="left:788px;top:162px"><h3>Equity financing</h3><p>Lorem ipsum dolor sit amet, consectetur adipiscing elit. Nam tempor faucibus ante, eget vulputate libero pharetra eu. Nulla at felis eros.</p></div>
  <div class="service left" style="left:84px;top:338px"><h3>Mezzanine</h3><p>Lorem ipsum dolor sit amet, consectetur adipiscing elit. Nam tempor faucibus ante, eget vulputate libero pharetra eu. Nulla at felis eros.</p></div>
  <div class="service" style="left:788px;top:338px"><h3>Perdorming</h3><p>Lorem ipsum dolor sit amet, consectetur adipiscing elit. Nam tempor faucibus ante, eget vulputate libero pharetra eu. Nulla at felis eros.</p></div>

  <svg class="svc-icon" style="left:450px;top:164px" viewBox="0 0 112 112"><circle cx="56" cy="56" r="54" fill="none" stroke="var(--teal)" stroke-width="2"/><circle cx="56" cy="56" r="42" fill="var(--teal)"/><rect x="38" y="46" width="34" height="20" rx="2" fill="none" stroke="#fff" stroke-width="3"/><circle cx="55" cy="56" r="4" fill="#fff"/><path d="M72 60h8" stroke="#fff" stroke-width="3"/></svg>
  <svg class="svc-icon" style="left:636px;top:164px" viewBox="0 0 112 112"><circle cx="56" cy="56" r="54" fill="none" stroke="var(--teal)" stroke-width="2"/><circle cx="56" cy="56" r="42" fill="var(--teal)"/><path d="M36 56 56 38 76 56" fill="none" stroke="#fff" stroke-width="3"/><path d="M42 54v20h28V54" fill="none" stroke="#fff" stroke-width="3"/><rect x="52" y="62" width="8" height="12" fill="#fff"/></svg>
  <svg class="svc-icon" style="left:450px;top:340px" viewBox="0 0 112 112"><circle cx="56" cy="56" r="54" fill="none" stroke="var(--teal)" stroke-width="2"/><circle cx="56" cy="56" r="42" fill="var(--teal)"/><circle cx="56" cy="48" r="13" fill="none" stroke="#fff" stroke-width="3"/><text x="56" y="54" text-anchor="middle" font-family="Lato,sans-serif" font-weight="700" font-size="16" fill="#fff">$</text><path d="M36 72h14l8 4h18" fill="none" stroke="#fff" stroke-width="3"/></svg>
  <svg class="svc-icon" style="left:636px;top:340px" viewBox="0 0 112 112"><circle cx="56" cy="56" r="54" fill="none" stroke="var(--teal)" stroke-width="2"/><circle cx="56" cy="56" r="42" fill="var(--teal)"/><rect x="38" y="62" width="7" height="12" fill="#fff"/><rect x="50" y="56" width="7" height="18" fill="#fff"/><rect x="62" y="50" width="7" height="24" fill="#fff"/><path d="M38 54 52 44 62 48 76 36" fill="none" stroke="#fff" stroke-width="3"/></svg>
</section>

<section class="team">
  <h2 class="heading" style="top:38px">Our Team</h2>
  <div class="heading-rule" style="top:96px"></div>
  <div class="member featured" style="left:79px"><div class="portrait" role="img" aria-label="Portrait of a team member"></div><h4>Surname Name</h4><span>Halden EECS Professor</span><i></i></div>
  <div class="member" style="left:348px"><div class="portrait" role="img" aria-label="Portrait of a team member"></div><h4>Surname Name</h4><span>Halden EECS Professor</span><i></i></div>
  <div class="member" style="left:616px"><div class="portrait" role="img" aria-label="Portrait of a team member"></div><h4>Surname Name</h4><span>Brightmoor Surgical Oncology</span><i></i></div>
  <div class="member" style="left:884px"><div class="portrait" role="img" aria-label="Portrait of a team member"></div><h4>Surname Name</h4><span>Brightmoor Radiology</span><i></i></div>
</section>

<section class="clients">
  <h2 class="heading" style="top:42px">What Our Client Say</h2>
  <div class="heading-rule" style="top:100px"></div>
  <div class="quote-card" style="left:79px"><svg class="quote-mark" viewBox="0 0 68 68"><circle cx="34" cy="34" r="34" fill="var(--teal)"/><path d="M22 28h10v10c0 6-4 9-8 10l-1-3c3-1 4-3 4-6h-5zM38 28h10v10c0 6-4 9-8 10l-1-3c3-1 4-3 4-6h-5z" fill="#fff"/></svg><p>Lorem Ipsum is simply dummy text of the printing and typesetting industry. Lorem Ipsum has been the industry.</p><em>-Commentetor Name</em></div>
  <div class="quote-card" style="left:438px"><svg class="quote-mark" viewBox="0 0 68 68"><circle cx="34" cy="34" r="34" fill="var(--teal)"/><path d="M22 28h10v10c0 6-4 9-8 10l-1-3c3-1 4-3 4-6h-5zM38 28h10v10c0 6-4 9-8 10l-1-3c3-1 4-3 4-6h-5z" fill="#fff"/></svg><p>Lorem Ipsum is simply dummy text of the printing and typesetting industry. Lorem Ipsum has been the industry.</p><em>-Commentetor Name</em></div>
  <div class="quote-card" style="left:799px"><svg class="quote-mark" viewBox="0 0 68 68"><circle cx="34" cy="34" r="34" fill="var(--teal)"/><path d="M22 28h10v10c0 6-4 9-8 10l-1-3c3-1 4-3 4-6h-5zM38 28h10v10c0 6-4 9-8 10l-1-3c3-1 4-3 4-6h-5z" fill="#fff"/></svg><p>Lorem Ipsum is simply dummy text of the printing and typesetting industry. Lorem Ipsum has been the industry.</p><em>-Commentetor Name</em></div>
</section>

<section class="news">
  <h2 class="heading" style="top:40px">Latest News</h2>
  <div class="heading-rule" style="top:98px"></div>
  <article class="article" style="left:79px"><div class="article-img" role="img" aria-label="Photo of business people meeting in an office"></div><div class="article-body"><div class="date"><b>29</b><small>APR</small></div><div><h5>Lorem Ipsum is simply dummy.</h5><p>Lorem Ipsum is simply dummy text of the printing and typesetting.</p></div></div></article>
  <article class="article" style="left:438px"><div class="article-img" role="img" aria-label="Photo of a business handshake"></div><div class="article-body"><div class="date"><b>29</b><small>APR</small></div><div><h5>Lorem Ipsum is simply dummy.</h5><p>Lorem Ipsum is simply dummy text of the printing and typesetting.</p></div></div></article>
  <article class="article" style="left:799px"><div class="article-img" role="img" aria-label="Photo of colleagues reviewing work at a laptop"></div><div class="article-body"><div class="date"><b>29</b><small>APR</small></div><div><h5>Lorem Ipsum is simply dummy.</h5><p>Lorem Ipsum is simply dummy text of the printing and typesetting.</p></div></div></article>
</section>

<section class="signup">
  <h3>To get latest updates and promotions signup now!</h3>
  <div class="field">Enter Your Email</div>
  <div class="go">Subscribe</div>
</section>

<footer class="site-footer">
  <div class="contact-box">
    <h4>Contact Detail</h4>
    <div class="contact-line"><svg width="18" height="20" viewBox="0 0 18 20"><path d="M9 1a6 6 0 0 0-6 6c0 5 6 12 6 12s6-7 6-12a6 6 0 0 0-6-6z" fill="var(--teal)"/><circle cx="9" cy="7" r="2.2" fill="var(--dark)"/></svg><span>Lorem Ipsum is simply dummy text of the printing.</span></div>
    <div class="contact-line"><svg width="18" height="18" viewBox="0 0 18 18"><path d="M4 1l3 4-2 2c1 2 3 4 5 5l2-2 4 3-2 3C8 16 2 10 1 4z" fill="var(--teal)"/></svg><span>123 456 7890</span></div>
    <div class="contact-line"><svg width="18" height="14" viewBox="0 0 18 14"><rect x="1" y="1" width="16" height="12" fill="none" stroke="var(--teal)" stroke-width="2"/><path d="M1 1l8 7 8-7" fill="none" stroke="var(--teal)" stroke-width="2"/></svg><span>info@orinventuresgroup.com</span></div>
  </div>
  <h3 class="quote-title">Request a Free Quote</h3>
  <div class="quote-rule"></div>
  <div class="input" style="left:445px;top:162px;width:283px;height:40px">Name</div>
  <div class="input" style="left:445px;top:214px;width:283px;height:40px">Email</div>
  <div class="input" style="left:445px;top:266px;width:283px;height:40px">Phone</div>
  <div class="input" style="left:747px;top:162px;width:296px;height:145px">Message</div>
  <div class="send"><svg width="63" height="145" viewBox="0 0 63 145"><path d="M20 73 44 62 38 86 32 77z" fill="#fff"/><path d="M32 77 44 62" stroke="var(--teal)" stroke-width="1.5"/></svg></div>
</footer>

<footer class="bottom">
  <div class="bottom-links"><span>Home</span><span>About</span><span>Team</span><span>Services</span><span>Project Experience</span><span>Contact</span></div>
  <p>©<b>ORIN VENTURES GROUP</b> - 2017. All Rights Reserved.</p>
</footer>

</body>
</html>
```